Assisted living facility needs a business card design

We need a business card design for an assisted living facility in Los Angeles. We have a logo selected but we would like a business card design that will leave a lasting impression on families looking to place their elderly loved ones in our care as well as on other facility providers who may refer their elderly residents to our facility.

```html
<!DOCTYPE html>
<html lang="en">
<head>
<meta charset="UTF-8">
<title>Harborview Gardens – Business Card</title>
<link href="https://fonts.googleapis.com/css2?family=Cormorant+Garamond:wght@500;600&display=swap" rel="stylesheet">
<style>
  :root {
    --brand-blue: #0277c2;
    --card-white: #ffffff;
    --backdrop: #ebeff1;
    --text-gray: #4a4f55;
  }
  html, body {
    margin: 0;
    width: 1200px;
    height: 1200px;
    overflow: hidden;
    background: var(--backdrop);
  }
  .canvas {
    position: relative;
    width: 1200px;
    height: 1200px;
  }
  .card {
    position: absolute;
    left: 222px;
    width: 819px;
    height: 469px;
    background: var(--card-white);
    border-radius: 36px;
    overflow: hidden;
  }
  .card--front { top: 56px; }
  .card--back { top: 644px; }
  .card__top-band {
    position: absolute;
    left: 0; top: 0;
    width: 100%;
    height: 63px;
    background: var(--brand-blue);
  }
  .card__bottom-band {
    position: absolute;
    left: 454px;
    bottom: 0;
    right: 0;
    height: 19px;
    background: var(--brand-blue);
    border-top-left-radius: 19px;
  }
  .card__divider {
    position: absolute;
    left: 454px;
    top: 96px;
    width: 2px;
    height: 320px;
    border-radius: 1px;
    background: var(--brand-blue);
  }
  .contact-list {
    position: absolute;
    left: 63px;
    top: 187px;
    margin: 0;
    padding: 0;
    list-style: none;
    display: flex;
    flex-direction: column;
    gap: 19px;
  }
  .contact-item {
    display: flex;
    align-items: center;
    gap: 16px;
    height: 38px;
  }
  .contact-icon {
    width: 38px;
    height: 38px;
    flex: none;
    display: block;
  }
  .contact-text {
    font-family: "Cormorant Garamond", serif;
    font-weight: 600;
    font-size: 17px;
    color: var(--text-gray);
    white-space: nowrap;
  }
  .brand-name {
    position: absolute;
    margin: 0;
    font-family: "Cormorant Garamond", serif;
    font-weight: 500;
    color: var(--brand-blue);
    text-transform: uppercase;
    white-space: nowrap;
    transform: translate(-50%, -50%);
  }
  .card--front .brand-name {
    left: 634px;
    top: 256px;
    font-size: 24px;
    letter-spacing: 1px;
  }
  .card--back .brand-name {
    left: 409px;
    top: 242px;
    font-size: 52px;
    letter-spacing: 2px;
  }
</style>
</head>
<body>
<div class="canvas">

  <section class="card card--front">
    <div class="card__top-band"></div>
    <ul class="contact-list">
      <li class="contact-item">
        <svg class="contact-icon" viewBox="0 0 38 38" aria-label="Phone">
          <circle cx="19" cy="19" r="19" fill="var(--brand-blue)"/>
          <path d="M12.5 10.5c1-.8 2-.6 2.6.3l1.6 2.6c.5.8.3 1.7-.4 2.2l-1 .7c.8 2 2.5 3.9 4.6 5l.8-1c.6-.7 1.5-.8 2.2-.3l2.5 1.7c.8.6.9 1.7.1 2.5l-1.2 1.2c-1 1-2.6 1.1-4 .4-4.1-2-7.1-5.3-8.8-9.6-.5-1.4-.2-3 .9-3.9z" fill="none" stroke="#fff" stroke-width="1.6" stroke-linejoin="round"/>
        </svg>
        <span class="contact-text">(555) 010-2040</span>
      </li>
      <li class="contact-item">
        <svg class="contact-icon" viewBox="0 0 38 38" aria-label="Email">
          <circle cx="19" cy="19" r="19" fill="var(--brand-blue)"/>
          <rect x="7" y="12" width="24" height="15" rx="1" fill="#fff"/>
          <path d="M7.8 12.8 19 21l11.2-8.2M7.8 26.2l8.6-7M30.2 26.2l-8.6-7" fill="none" stroke="var(--brand-blue)" stroke-width="1.1"/>
        </svg>
        <span class="contact-text">hello@harborviewgardens.com</span>
      </li>
      <li class="contact-item">
        <svg class="contact-icon" viewBox="0 0 38 38" aria-label="Address">
          <circle cx="19" cy="19" r="19" fill="var(--brand-blue)"/>
          <path d="M19 9a7 7 0 0 0-7 7c0 4.5 7 13 7 13s7-8.5 7-13a7 7 0 0 0-7-7z" fill="#fff"/>
          <circle cx="19" cy="15.5" r="2.6" fill="var(--brand-blue)"/>
        </svg>
        <span class="contact-text">1420 Maple Crest Ave, Los Angeles, CA</span>
      </li>
      <li class="contact-item">
        <svg class="contact-icon" viewBox="0 0 38 38" aria-label="Website">
          <circle cx="19" cy="19" r="19" fill="var(--brand-blue)"/>
          <g fill="none" stroke="#fff" stroke-width="1.1">
            <circle cx="19" cy="19" r="11"/>
            <ellipse cx="19" cy="19" rx="4.8" ry="11"/>
            <line x1="19" y1="8" x2="19" y2="30"/>
            <line x1="8" y1="19" x2="30" y2="19"/>
            <path d="M10 13.5h18M10 24.5h18"/>
          </g>
        </svg>
        <span class="contact-text">www.harborviewgardens.com</span>
      </li>
    </ul>
    <div class="card__divider"></div>
    <h2 class="brand-name">Harborview Gardens</h2>
    <div class="card__bottom-band"></div>
  </section>

  <section class="card card--back">
    <div class="card__top-band"></div>
    <h1 class="brand-name">Harborview Gardens</h1>
    <div class="card__bottom-band"></div>
  </section>

</div>
</body>
</html>
```